Ledger Lantern - Website Design

Create website designs for new LedgerLantern.com web application.
We are looking for a clean, playful design based on the attached wireframes and the images we have collected on our PinBoardly board for inspiration : https://app.pinboardly-example.net/7QzRt2mK4wPa91?p=3Hbn8YcLd5R
Users of the site will want to be able to quickly run a search using the transaction descriptor they want to identify and see any matching merchants. If they don't get a match then we need then to be able to easily provide further details so we can try and find a match for them
Updates
Target Market(s)
Anyone with a bank account
Number of Pages Required
5+ page
Requirements
Must have
- Clean yet playful design, incorporating the themes from our pinboardly board

```html
<!DOCTYPE html>
<html lang="en">
<head>
<meta charset="utf-8">
<title>Ledger Lantern – Website Design</title>
<link href="https://fonts.googleapis.com/css2?family=Hind:wght@400;500&family=Arimo:wght@400;700&display=swap" rel="stylesheet">
<style>
  :root{
    --backdrop:#6e6e6e;
    --backdrop-edge:#555555;
    --sky-top:#3f8fcf;
    --sky-mid:#cfe6f7;
    --sky-low:#e6f2fb;
    --brand:#1d5d8c;
    --teal:#1a8f8a;
    --ink:#2f3a44;
    --muted:#4a5560;
    --line:#cfd8df;
    --panel:#ffffff;
    --pill:#cfe3ea;
    --alert:#e5363c;
    --coat:#c4884a;
    --coat-dark:#6a6a64;
  }
  *{box-sizing:border-box;margin:0;padding:0}
  html,body{width:1200px;height:858px;overflow:hidden}
  body{
    background:radial-gradient(ellipse at 50% 50%,var(--backdrop) 0%,var(--backdrop-edge) 100%);
    font-family:"Arimo",Arial,sans-serif;color:var(--ink);position:relative;
  }
  .screen{
    position:absolute;width:521px;height:355px;overflow:hidden;
    box-shadow:0 10px 28px rgba(0,0,0,.45);
  }
  .screen--home{left:66px;top:63px}
  .screen--suggest{left:612px;top:63px}
  .screen--results{left:66px;top:439px}
  .screen--nomatch{left:612px;top:439px}

  .sky{
    position:absolute;inset:0;
    background:
      radial-gradient(ellipse 140px 40px at 120px 40px,rgba(255,255,255,.85),transparent 70%),
      radial-gradient(ellipse 160px 45px at 400px 60px,rgba(255,255,255,.8),transparent 70%),
      radial-gradient(ellipse 120px 40px at 60px 230px,rgba(255,255,255,.6),transparent 70%),
      linear-gradient(160deg,var(--sky-top) 0%,var(--sky-mid) 35%,var(--sky-low) 70%,#d8ecf8 100%);
  }
  .skyline{
    position:absolute;left:71px;top:206px;width:360px;height:149px;
    background:linear-gradient(180deg,rgba(159,182,200,0) 0%,rgba(159,182,200,.35) 60%,rgba(159,182,200,.5) 100%);
  }
  .detective{
    position:absolute;left:430px;top:164px;width:84px;height:191px;border-radius:30px 30px 4px 4px;
    background:linear-gradient(180deg,#8a5a34 0%,var(--coat) 35%,var(--coat) 60%,var(--coat-dark) 100%);
  }

  .brand{position:absolute;left:0;right:0;display:flex;align-items:center;justify-content:center;gap:7px}
  .brand__dot{width:26px;height:26px;border-radius:50%;flex:none;background:var(--brand)}
  .brand__name{font-family:"Hind",sans-serif;font-weight:500;font-size:31px;line-height:1;color:var(--brand);padding-top:5px}
  .tagline{position:absolute;left:0;right:0;text-align:center;font-size:8.4px;line-height:12.4px;color:var(--muted)}

  .search{
    position:absolute;left:109px;width:303px;height:30px;border-radius:15px;
    background:var(--panel);border:1.5px solid var(--line);
    display:flex;align-items:center;padding-left:18px;font-size:6.2px;color:var(--ink);
  }
  .search__button{
    position:absolute;right:7px;top:50%;margin-top:-8.5px;width:17px;height:17px;border-radius:50%;
    background:linear-gradient(135deg,var(--brand),var(--teal));
    display:flex;align-items:center;justify-content:center;
  }
  .search--open{height:82px;border-radius:14px;display:block;padding:0}
  .search--open .search__input{height:30px;display:flex;align-items:center;padding-left:15px;border-bottom:1px solid var(--line)}
  .search--open .search__button{top:9px;margin-top:0}
  .suggestions{list-style:none;padding:6px 0 0 16px}
  .suggestions li{font-size:5px;line-height:12.4px;color:var(--ink);text-decoration:underline}

  .help-link{position:absolute;right:134px;font-size:5.8px;color:var(--brand);text-decoration:underline}

  .section-title{position:absolute;left:116px;top:155px;font-weight:700;font-size:10.5px;color:var(--brand)}
  .matches{
    position:absolute;left:109px;top:175px;width:303px;height:82px;background:var(--panel);
    border:1.5px solid var(--line);border-radius:10px;overflow:hidden;
    border-collapse:separate;border-spacing:0;font-size:4.9px;
  }
  .matches th,.matches td{text-align:left;padding-left:15px;border-bottom:1px solid var(--line);height:20px}
  .matches th{font-weight:700;font-size:4.8px;height:22px}
  .matches tr:last-child td{border-bottom:none}
  .matches th:nth-child(1),.matches td:nth-child(1){width:116px;border-right:1px solid var(--line)}
  .matches th:nth-child(2),.matches td:nth-child(2){width:98px;border-right:1px solid var(--line)}
  .matches td:nth-child(3){padding-left:18px}
  .pill{display:inline-block;width:44px;height:14px;line-height:14px;border-radius:7px;background:var(--pill);color:var(--brand);font-size:4.2px;font-weight:700;text-align:center}

  .crowd{
    position:absolute;left:109px;width:303px;background:var(--panel);
    border:1.5px solid var(--line);border-radius:12px;text-align:center;
    font-size:5.8px;line-height:9px;color:var(--ink);padding-top:9px;
  }
  .crowd__button{
    display:inline-block;margin-top:5px;width:83px;height:15px;line-height:15px;border-radius:8px;
    background:linear-gradient(90deg,var(--brand),var(--teal));color:#fff;font-size:4.4px;font-weight:700;
  }
  .no-match{position:absolute;left:0;right:0;top:203px;text-align:center;font-size:16px;color:var(--alert)}
</style>
</head>
<body>

<!-- Home -->
<section class="screen screen--home">
  <div class="sky" role="img" aria-label="Soft blue sky with white clouds"></div>
  <div class="skyline" role="img" aria-label="Line-art city skyline"></div>
  <div class="detective" role="img" aria-label="Cartoon detective in trench coat holding a magnifying glass"></div>
  <div class="brand" style="top:78px">
    <span class="brand__dot"></span>
    <span class="brand__name">Ledger Lantern</span>
  </div>
  <p class="tagline" style="top:125px">Helping you identify those odd and sometimes surprising charges on your<br>bank statements and transaction feeds!</p>
  <div class="search" style="top:166px">Enter your transaction descriptor...
    <span class="search__button"><svg width="6" height="4" viewBox="0 0 6 4"><polyline points="0.8,0.8 3,3 5.2,0.8" fill="none" stroke="#fff" stroke-width="1.1"/></svg></span>
  </div>
  <a class="help-link" style="top:200px">What is a Transaction Descriptor?</a>
</section>

<!-- Suggestions -->
<section class="screen screen--suggest">
  <div class="sky" role="img" aria-label="Soft blue sky with white clouds"></div>
  <div class="skyline" role="img" aria-label="Line-art city skyline"></div>
  <div class="detective" role="img" aria-label="Cartoon detective in trench coat holding a magnifying glass"></div>
  <div class="brand" style="top:78px">
    <span class="brand__dot"></span>
    <span class="brand__name">Ledger Lantern</span>
  </div>
  <p class="tagline" style="top:125px">Helping you identify those odd and sometimes surprising charges on your<br>bank statements and transaction feeds!</p>
  <div class="search search--open" style="top:169px">
    <div class="search__input">WOOLG</div>
    <span class="search__button"><svg width="6" height="4" viewBox="0 0 6 4"><polyline points="0.8,0.8 3,3 5.2,0.8" fill="none" stroke="#fff" stroke-width="1.1"/></svg></span>
    <ul class="suggestions">
      <li>WOOLGROVE PTY LTD ST IVES AU</li>
      <li>WOOLGROVE ONLINE SERVICES AU220223</li>
      <li>WOOLGATE CLOTHING CO SYDNEY</li>
    </ul>
  </div>
</section>

<!-- Results -->
<section class="screen screen--results">
  <div class="sky" role="img" aria-label="Soft blue sky with white clouds"></div>
  <div class="skyline" role="img" aria-label="Line-art city skyline"></div>
  <div class="detective" role="img" aria-label="Cartoon detective in trench coat holding a magnifying glass"></div>
  <div class="brand" style="top:26px">
    <span class="brand__dot"></span>
    <span class="brand__name">Ledger Lantern</span>
  </div>
  <p class="tagline" style="top:74px">Helping you identify those odd and sometimes surprising charges on your<br>bank statements and transaction feeds!</p>
  <div class="search" style="top:115px">WOOLGROVE PTY LTD ST IVES AU
    <span class="search__button"><svg width="6" height="4" viewBox="0 0 6 4"><polyline points="0.8,0.8 3,3 5.2,0.8" fill="none" stroke="#fff" stroke-width="1.1"/></svg></span>
  </div>
  <a class="help-link" style="top:149px">What is a Transaction Descriptor?</a>
  <h2 class="section-title">Top Matches</h2>
  <table class="matches">
    <tr><th>MERCHANT NAME</th><th>CONFDENCE</th><th></th></tr>
    <tr><td>Woolgrove Pty Ltd</td><td>High</td><td><span class="pill">VIEW DETAILS</span></td></tr>
    <tr><td>Woolgate Clothing Co</td><td>Low</td><td><span class="pill">VIEW DETAILS</span></td></tr>
    <tr><td>Woolgrove Online Plc</td><td>Low</td><td><span class="pill">VIEW DETAILS</span></td></tr>
  </table>
  <div class="crowd" style="top:267px;height:57px">
    Couldn't fnd a match? Help us Crowd Source more data by clicking the button below and<br>providing a few details so we can help fnd it and make it available to everyone.<br>
    <span class="crowd__button">HELP IMPROVE OUR RESULTS</span>
  </div>
</section>

<!-- No match -->
<section class="screen screen--nomatch">
  <div class="sky" role="img" aria-label="Soft blue sky with white clouds"></div>
  <div class="skyline" role="img" aria-label="Line-art city skyline"></div>
  <div class="detective" role="img" aria-label="Cartoon detective in trench coat holding a magnifying glass"></div>
  <div class="brand" style="top:52px">
    <span class="brand__dot"></span>
    <span class="brand__name">Ledger Lantern</span>
  </div>
  <p class="tagline" style="top:100px">Helping you identify those odd and sometimes surprising charges on your<br>bank statements and transaction feeds!</p>
  <div class="search" style="top:141px">WOOLGROVE PTY LTD ST IVES AU
    <span class="search__button"><svg width="6" height="4" viewBox="0 0 6 4"><polyline points="0.8,0.8 3,3 5.2,0.8" fill="none" stroke="#fff" stroke-width="1.1"/></svg></span>
  </div>
  <a class="help-link" style="top:175px">What is a Transaction Descriptor?</a>
  <p class="no-match">Hmmm, we couldn't fnd a match!</p>
  <div class="crowd" style="top:241px;height:57px">
    Couldn't fnd a match? Help us Crowd Source more data by clicking the button below and<br>providing a few details so we can help fnd it and make it available to everyone.<br>
    <span class="crowd__button">HELP IMPROVE OUR RESULTS</span>
  </div>
</section>

</body>
</html>
```